Business Card Design

Contact Information for Business Card

A vertical business card request- a medium & light gray with silverpine tree logo (logo is attached)

Please use Trebuchet font -- if possible- can we use two different color gray? (See pictures attached below)
Info on the front should be the Silverpine tree logo - on the top of the card, followed by the info ...
Card to read: " " indicated what should be on the card --
Name: " Carla Merrow "
Title : "Partner "
" Office: 202.555.0147 "
" Mobile: 202.555.0183 "

Backside of the card - solid medium color gray color w/ address and small message centered in the card - Trebuchet font
to read:

" 718 B North Larkmoor Avenue, NE "
" Washington, DC 20019 "

Then below address to read:
" Fundraising | Event Planning | Political Consulting "

```html
<!DOCTYPE html>
<html lang="en">
<head>
<meta charset="utf-8">
<title>Silverpine Strategies – Business Card</title>
<link rel="stylesheet" href="https://fonts.googleapis.com/css2?family=PT+Sans:wght@400&display=swap">
<style>
  :root {
    --backdrop: #141414;
    --card: #ffffff;
    --gray-medium: #646464;
    --gray-light: #b9b9b9;
    --gray-text: #3d3d3d;
    --tree-tone: #6a6a6a;
    --on-gray: #ffffff;
  }
  * { margin: 0; padding: 0; box-sizing: border-box; }
  html, body {
    width: 1200px; height: 900px; overflow: hidden;
    background: var(--backdrop);
    font-family: "PT Sans", "Trebuchet MS", sans-serif;
  }
  .stage { position: relative; width: 1200px; height: 900px; }

  .card {
    position: absolute; top: 230px;
    width: 271px; height: 440px;
    border-radius: 10px; overflow: hidden;
  }
  .card--front { left: 309px; background: var(--card); }
  .card--back { left: 620px; background: var(--gray-medium); }

  /* Front */
  .brand-panel {
    position: absolute; left: 0; top: 0; width: 100%; height: 170px;
    background: var(--gray-medium);
    display: flex; align-items: flex-end; justify-content: center;
    padding-bottom: 26px;
  }
  .brand-name {
    color: var(--on-gray); text-align: center;
    font-size: 20px; line-height: 24px; letter-spacing: 1px;
  }
  .brand-name span { display: block; }
  .accent-band {
    position: absolute; left: 0; top: 176px; width: 100%; height: 10px;
    background: var(--gray-light);
  }
  .tree-art { position: absolute; right: 0; bottom: 0; width: 96px; height: 230px; }

  .contact { position: absolute; left: 28px; top: 236px; color: var(--gray-text); }
  .contact-name { font-size: 18px; line-height: 22px; }
  .contact-title { font-size: 13px; line-height: 16px; }
  .contact-phones { list-style: none; margin-top: 24px; font-size: 13px; }
  .contact-phones li { display: flex; align-items: center; height: 22px; }
  .contact-phones .label { width: 50px; }
  .contact-phones svg { width: 9px; height: 10px; margin-right: 7px; fill: var(--gray-text); }

  /* Back */
  .back-content {
    position: absolute; inset: 0;
    display: flex; flex-direction: column; align-items: center; justify-content: center;
    color: var(--on-gray); text-align: center;
  }
  .address { font-size: 13px; line-height: 18px; }
  .divider { width: 40px; height: 1px; background: var(--gray-light); margin: 22px 0; }
  .services { list-style: none; font-size: 15px; line-height: 26px; }
</style>
</head>
<body>
<main class="stage">
  <section class="card card--front" aria-label="Card front">
    <div class="brand-panel">
      <p class="brand-name">SILVERPINE <span>STRATEGIES</span></p>
    </div>
    <div class="accent-band"></div>
    <svg class="tree-art" role="img" aria-label="Gray bare tree silhouette" viewBox="0 0 96 230" preserveAspectRatio="none">
      <defs>
        <linearGradient id="treeFade" x1="1" y1="1" x2="0" y2="0">
          <stop offset="0" stop-color="#6a6a6a" stop-opacity="0.4"/>
          <stop offset="1" stop-color="#6a6a6a" stop-opacity="0"/>
        </linearGradient>
      </defs>
      <rect width="96" height="230" fill="url(#treeFade)"/>
    </svg>
    <div class="contact">
      <p class="contact-name">Carla Merrow</p>
      <p class="contact-title">Partner</p>
      <ul class="contact-phones">
        <li><svg viewBox="0 0 10 10" aria-hidden="true"><path d="M2 0.5 L3.6 2.6 L2.7 3.6 Q3.8 5.9 6.3 7.2 L7.3 6.3 L9.5 8 L8.3 9.5 Q2.2 8.3 0.5 1.7 Z"/></svg><span class="label">Office:</span>202.555.0147</li>
        <li><svg viewBox="0 0 10 10" aria-hidden="true"><path d="M2.5 0 H7.5 V10 H2.5 Z M3.5 1.2 V8 H6.5 V1.2 Z"/></svg><span class="label">Mobile:</span>202.555.0183</li>
      </ul>
    </div>
  </section>

  <section class="card card--back" aria-label="Card back">
    <div class="back-content">
      <p class="address">718 B North Larkmoor Avenue, NE<br>Washington, DC 20019</p>
      <div class="divider"></div>
      <ul class="services">
        <li>Fundraising</li>
        <li>Event Planning</li>
        <li>Political Consulting</li>
      </ul>
    </div>
  </section>
</main>
</body>
</html>
```